Holiday Rental Company Flyer Design (DL not A5)

Note from PixelFolk Administration: The category sizing selected is A5, however the project requires DL sized artwork. Please refer to the DL template link below while the 'Special Requirements' are updated accordingly.

Project Brief:
We need a double sided DL flyer designed for an up market Holiday Rental Company that portrays a personalised approach to property management. These are to be used for letter box drops to homes we're specifically targeting so the design should be modern, complimentary colour palette, uncluttered & visually appealing.

Please Download the DL Template from Quillmark here: http://www.quillmark.com.au/qm/ns/propath/UploadResources.aspx?selectedTab=0?pfid=BFB&pf_id=BFB&xnav=easypath-upload-image#Templates

Target Market(s)

Wealthy Home Owners

Industry/Entity Type

It Company

Font styles to use
Other font styles liked:
• Avant Garde Extra Light & Demi

Colors
33b8a4

Requirements
Must have
• DL Flyer sizes (210mm width x 99mm width, plus 3mm bleed)
• Front: Logo, Main Image & Grab
• Back: Contact Details & Brief Description of our business
• Images: Ideally the main image should be the house with the pool but alternatively a lifestyle images could also be used.
Nice to have
• A creative designer!
Should not have
• Clutter & busy designs

```html
<!DOCTYPE html>
<html lang="en">
<head>
<meta charset="utf-8">
<title>Harbour Retreats – DL Flyer</title>
<link rel="stylesheet" href="https://fonts.googleapis.com/css2?family=Lato:ital,wght@0,400;0,700;1,400&family=Raleway:wght@200;300&family=Anton&display=swap">
<style>
  :root{
    --teal:#33b8a4;
    --teal-deep:#23a895;
    --navy:#1c1a4a;
    --navy-deep:#141238;
    --white:#ffffff;
    --stage:#2a2a2a;
  }
  *{box-sizing:border-box;margin:0;padding:0}
  html,body{width:1200px;height:1185px;overflow:hidden;background:var(--stage)}
  .canvas{position:relative;width:1200px;height:1185px}

  .flyer{position:absolute;width:518px;height:1098px;overflow:hidden}
  .flyer--back{left:67px;top:57px;background:var(--teal);font-family:"Lato",sans-serif;color:var(--white)}
  .flyer--front{left:623px;top:59px;background:var(--navy)}

  /* back */
  .sea-photo{position:absolute;left:0;top:0;width:518px;height:600px;
    background:linear-gradient(180deg,#3fc4cc 0%,#2aa8b8 35%,#3ab7b9 60%,#4cc5bd 100%)}
  .back-frame{position:absolute;left:30px;top:33px;width:453px;height:520px;border:1px solid rgba(255,255,255,.75);
    background:rgba(40,140,170,.18)}
  .back-title{position:absolute;left:0;top:96px;width:518px;text-align:center;font-weight:700;font-size:31px;letter-spacing:-.3px}
  .back-copy{position:absolute;left:0;width:518px;text-align:center;font-size:15.5px;line-height:22px}
  .back-copy--intro{top:153px}
  .back-copy--service{top:264px}
  .back-copy--list{top:353px}

  .room-photo{position:absolute;border-radius:50%;border:7px solid var(--white)}
  .room-photo--lounge{left:3px;top:497px;width:256px;height:256px;background:radial-gradient(circle at 50% 45%,#e2c9a6,#a28e74 70%,#5f5a52)}
  .room-photo--bath{left:255px;top:492px;width:256px;height:256px;background:radial-gradient(circle at 55% 40%,#d9d9d6,#b7b5ae 65%,#8e8c87)}
  .room-photo--bed{left:138px;top:655px;width:250px;height:250px;background:linear-gradient(160deg,#f3dcb4 0%,#e7c98f 40%,#e0d84a 65%,#c86a4e 100%)}

  .contact-lead{position:absolute;left:0;top:908px;width:518px;text-align:center;font-style:italic;font-size:15.5px;line-height:21px}
  .contact-phone{position:absolute;left:0;top:958px;width:518px;text-align:center;font-weight:700;font-size:44px}
  .contact-post{position:absolute;left:0;top:1021px;width:518px;text-align:center;font-weight:700;font-size:16px}
  .contact-email{position:absolute;left:0;top:1045px;width:518px;text-align:center;font-size:16px}

  /* front */
  .front-band{position:absolute;left:0;top:0;width:518px;height:320px}
  .brand-name{position:absolute;left:0;top:74px;width:518px;text-align:center;font-family:"Raleway",sans-serif;
    font-weight:200;font-size:48px;line-height:48px;letter-spacing:4px;color:var(--white)}
  .brand-mark{position:absolute;left:239px;top:202px;width:40px;height:40px;border-radius:50%;border:1.5px solid var(--white)}
  .headline{position:absolute;left:0;top:340px;width:518px;text-align:center;font-family:"Anton",sans-serif;font-size:84px;line-height:100px;color:var(--white);letter-spacing:-1px}
  .subline{position:absolute;left:0;top:438px;width:518px;text-align:center;font-family:"Raleway",sans-serif;font-weight:300;font-size:31px;line-height:36px;color:var(--white);letter-spacing:.5px}
  .house-photo{position:absolute;left:0;top:530px;width:518px;height:568px;
    background:linear-gradient(180deg,var(--navy) 0%,#3a3470 25%,#5b4f86 45%,#8d7a88 62%,#c8a978 78%,#3f9fd8 90%,#2f7fc0 100%)}
  .front-frame{position:absolute;left:38px;top:41px;width:442px;height:1018px;border:1px solid rgba(255,255,255,.8)}
  .web-bar{position:absolute;left:38px;top:1023px;width:442px;height:36px;background:var(--white);
    text-align:center;font-family:"Raleway",sans-serif;font-weight:300;font-size:12px;line-height:36px;letter-spacing:1.5px;color:var(--teal-deep)}
</style>
</head>
<body>
<main class="canvas">

  <section class="flyer flyer--back">
    <div class="sea-photo" role="img" aria-label="Seals swimming in clear turquoise sea"></div>
    <div class="back-frame"></div>
    <h2 class="back-title">What We Do Differently!</h2>
    <p class="back-copy back-copy--intro">Rather than relying upon a key safe or<br>a central pick-up destination,<br>a ‘Harbour Retreats’ staff member<br>will greet guests upon arrival.</p>
    <p class="back-copy back-copy--service">Our ‘Meet &amp; Greet’ service provides<br>home owners with an increased level of<br>Security &amp; also allows us to:</p>
    <p class="back-copy back-copy--list">Prepare the home for their arrival<br>(lights, heaters, music etc.)<br>Establish a rapport &amp; help facilitate future bookings<br>Reiterate their responsibilities to<br>ensure the return of their bond</p>

    <div class="room-photo room-photo--lounge" role="img" aria-label="Bird of paradise flowers in a glass vase"></div>
    <div class="room-photo room-photo--bath" role="img" aria-label="White orchid beside a modern bathroom basin"></div>
    <div class="room-photo room-photo--bed" role="img" aria-label="Bed with yellow cushions and a colourful quilt"></div>

    <p class="contact-lead">If you’d like to know what your property<br>could achieve or require additional information, please contact us on:</p>
    <p class="contact-phone">(03)5550 2741</p>
    <p class="contact-post">PO Box 18, Elmsford Victoria 3999</p>
    <p class="contact-email">email: stay@harbourretreats.com.au</p>
  </section>

  <section class="flyer flyer--front">
    <div class="house-photo" role="img" aria-label="Modern house lit at dusk with an illuminated pool"></div>
    <svg class="front-band" viewBox="0 0 518 320" aria-hidden="true">
      <polygon fill="#33b8a4" points="0,0 518,0 518,178 370,224 358,224 358,250 259,316 160,250 160,224 148,224 0,178"/>
    </svg>
    <div class="front-frame"></div>
    <h1 class="brand-name">HARBOUR<br>RETREATS</h1>
    <span class="brand-mark"></span>
    <p class="headline">HOLIDAY</p>
    <p class="subline">RENTAL MANAGEMENT<br>WITH A DIFFERENCE</p>
    <p class="web-bar">harbourretreats.com.au</p>
  </section>

</main>
</body>
</html>
```